Flyer-Design für Aufbereiter von Fahrzeugen
Zielgruppe
Wir reinigen und aufbereiten (polieren, versiegeln) Fahrzeuge, vorwiegend Autos. Zusätzlich leihen wir Personal an Autowerkstätten für Servicereinigungen und Fahrzeugaufbereitung an. Unsere Kunden sind Privatpersonen: Junge Autofan aus der Tuningszene und gutsituierte mit Luxusautos. Weitere Kunden sind Gewerbliche für professionelle Fahrzeugaufbereitung und Manpower ausleihen.
Hier finden Sie unsere Tätigkeiten https://www.glanzwerk-muster.ch/unsere-leistungen/
Aufgabenstellung
Mit diesem Flyer wollen wir im besonderen die private Kundschaft ansprechen: Fahrzeugreinigung und -aufbereitung mit Hightech-Ergebnis. Der Flyer, A4, legen wir 1x zusammen und in ein durchsichtiges Couvert C5, sodass von beiden Seiten der Flyer gelesen werden kann. Wir verteilen ihn meistens nach einem Gespräch an Interessierte. Auf der Rückseite der Visitenkarte steht bei uns "Treten Sie glänzend auf..." und auf dem TShirt steht seitlich "we clean your dream" leuchtgrün/gelb. Die Internetseite ist mal so eine Erstausgabe, welche wir in einem späteren Zeitpunkt auch nochmals updaten wollen.
Bei Verwendung von Foto Nr. 123122 bitte Uhr entfernen

```html
<!DOCTYPE html>
<html lang="de">
<head>
<meta charset="utf-8">
<title>Glanzwerk – High-End Fahrzeugaufbereitung</title>
<link href="https://fonts.googleapis.com/css2?family=Fira+Sans+Condensed:wght@600;700;800;900&family=Fira+Sans:wght@400&display=swap" rel="stylesheet">
<style>
  :root{
    --green:#7dc243;
    --green-light:#d6eac0;
    --ink:#111111;
    --paper:#ffffff;
    --stage:#f2f2f2;
    --footer-dark:#1c1c1c;
  }
  *{box-sizing:border-box;margin:0;padding:0}
  html,body{width:1200px;height:1200px;overflow:hidden;background:var(--stage)}
  .flyer{
    position:absolute;left:215px;top:58px;width:770px;height:1089px;
    background:var(--paper);overflow:hidden;
    font-family:"Fira Sans Condensed",sans-serif;color:var(--ink);
  }
  .brand{
    position:absolute;left:80px;top:58px;z-index:3;
    font-family:"Fira Sans",sans-serif;font-weight:400;font-size:34px;line-height:1;
    color:var(--green);letter-spacing:1px;display:flex;align-items:center;gap:10px;
  }
  .brand-dot{width:14px;height:14px;border-radius:50%;background:var(--green)}
  .headline{
    position:absolute;left:44px;top:138px;z-index:2;
    transform:rotate(-3deg);transform-origin:left top;
    font-weight:900;text-transform:uppercase;line-height:.8;
  }
  .headline .l1{font-size:128px;letter-spacing:-1px;display:block}
  .headline .l2{font-size:118px;display:block;margin-left:18px}
  .headline .l3{font-size:92px;display:block;margin-left:30px;margin-top:4px}
  .badge{
    position:absolute;left:560px;top:105px;width:190px;height:190px;border-radius:50%;z-index:1;
    background:var(--green);display:flex;align-items:center;justify-content:center;text-align:center;
    font-weight:800;font-size:22px;line-height:1.1;text-transform:uppercase;transform:rotate(-4deg);
  }
  .car-photo{position:absolute;left:0;top:410px;width:770px;height:620px}
  .benefits{position:absolute;left:0;top:488px;width:320px;z-index:2}
  .benefit{
    position:absolute;left:-10px;width:320px;padding:0 20px;
    display:flex;align-items:center;justify-content:center;text-align:center;
    font-weight:700;font-size:15.5px;line-height:1.35;text-transform:uppercase;
    border-radius:0 10px 10px 0;transform:rotate(-3deg);transform-origin:left center;
    box-shadow:0 3px 6px rgba(0,0,0,.25);
  }
  .benefit.strong{background:var(--green)}
  .benefit.soft{background:var(--green-light)}
  .inset-photo{
    position:absolute;left:522px;top:742px;width:220px;height:220px;border-radius:50%;
    border:7px solid var(--green);overflow:hidden;z-index:2;
  }
  .contact-bar{
    position:absolute;left:0;bottom:0;width:770px;height:80px;z-index:2;
    background:linear-gradient(180deg,rgba(28,28,28,0) 0%,var(--footer-dark) 45%);
    display:flex;align-items:flex-end;justify-content:center;padding-bottom:32px;
    color:#fff;font-weight:700;font-size:17px;letter-spacing:.4px;word-spacing:2px;
  }
  .contact-bar .sep{margin:0 10px}
</style>
</head>
<body>
<div class="flyer">
  <svg class="car-photo" role="img" aria-label="Foto: silberner Sportwagen von vorne seitlich mit Chromfelge" viewBox="0 0 770 620">
    <defs>
      <linearGradient id="carTone" x1="0" y1="0" x2="1" y2="1">
        <stop offset="0" stop-color="#f4f4f4"/>
        <stop offset=".5" stop-color="#d2d2d2"/>
        <stop offset="1" stop-color="#6e6e6e"/>
      </linearGradient>
    </defs>
    <rect width="770" height="620" fill="url(#carTone)"/>
  </svg>

  <div class="brand"><span class="brand-dot"></span>glanzwerk-muster.ch</div>

  <div class="badge">Profitieren<br>Sie von<br>unserem Können.<br>Sprechen Sie<br>uns an!</div>

  <h1 class="headline">
    <span class="l1">High-End</span>
    <span class="l2">Fahrzeug-</span>
    <span class="l3">Aufbereitung</span>
  </h1>

  <div class="benefits">
    <p class="benefit strong" style="top:0;height:88px">Wir arbeiten<br>professionell, setzen auf<br>High-End-Qualität</p>
    <p class="benefit soft" style="top:104px;height:82px">Mit uns gewinnen Sie Zeit.<br>Anruf genügt, alles übrige<br>erledigen wir</p>
    <p class="benefit strong" style="top:210px;height:76px">Mit uns sparen Sie Geld. Weniger<br>Fixkosten, variable nur bei Bedarf</p>
    <p class="benefit soft" style="top:306px;height:70px">Entlasten Sie sich. Wir übernehmen<br>Verantwortung für unseren Arbeit</p>
    <p class="benefit strong" style="top:392px;height:84px">Wir desinfizieren &amp; Geruchs-<br>neutralisieren Fahrzeuginnenraum<br>und Klimaanlage</p>
  </div>

  <svg class="inset-photo" role="img" aria-label="Foto: Hand im Handschuh reinigt Armaturenbrett mit Schwamm" viewBox="0 0 206 206">
    <defs>
      <radialGradient id="insetTone" cx=".45" cy=".45" r=".7">
        <stop offset="0" stop-color="#e9ecef"/>
        <stop offset=".6" stop-color="#9aa2a8"/>
        <stop offset="1" stop-color="#4a3a34"/>
      </radialGradient>
    </defs>
    <rect width="206" height="206" fill="url(#insetTone)"/>
  </svg>

  <footer class="contact-bar">
    <span>H 076 000 12 34</span><span class="sep">|</span>
    <span>F 041 000 56 7</span><span class="sep">|</span>
    <span>info@glanzwerk-muster.ch</span><span class="sep">|</span>
    <span>www.glanzwerk-muster.ch</span>
  </footer>
</div>
</body>
</html>
```